Business Card For Kelmora Financial Consulting

Hi, I would like a business card designed. Bold, modern.
Please use the same design as the logo. I have also attached the website design to see the overall theme.
Wordmark Font
Color: Hex: #01AEF7

```html
<!DOCTYPE html>
<html lang="en">
<head>
<meta charset="utf-8">
<title>Kelmora Financial Consulting – Business Card</title>
<link href="https://fonts.googleapis.com/css2?family=Source+Sans+3:wght@400;600;700&display=swap" rel="stylesheet">
<style>
  :root {
    --backdrop: #e4e4e4;
    --card: #13212b;
    --card-tint: #1b2f3c;
    --brand-blue: #01aef7;
    --accent-blue: #2a9fd6;
    --ink-light: #f2f4f5;
    --ink-soft: #dfe5e8;
  }
  * { margin: 0; padding: 0; box-sizing: border-box; }
  html, body {
    width: 1200px;
    height: 960px;
    overflow: hidden;
  }
  body {
    background: var(--backdrop);
    font-family: "Source Sans 3", "Source Sans Pro", sans-serif;
    position: relative;
  }
  .card {
    position: absolute;
    left: 298px;
    width: 606px;
    height: 346px;
    background: var(--card);
    overflow: hidden;
  }
  .card--front { top: 110px; }
  .card--back { top: 510px; }

  .front-texture {
    position: absolute;
    inset: 0;
    background: linear-gradient(100deg, #5d6a72 0%, #33424c 22%, #1c2b35 45%, #14222c 70%, #101c25 100%);
  }

  .wordmark {
    position: absolute;
    display: flex;
    align-items: center;
    gap: 12px;
  }
  .wordmark__square {
    flex: none;
    border: 3px solid var(--brand-blue);
  }
  .wordmark__name {
    color: var(--ink-light);
    font-weight: 700;
    text-transform: uppercase;
    line-height: 1;
    white-space: nowrap;
  }
  .card--front .wordmark {
    left: 145px;
    top: 148px;
    padding: 6px 14px 6px 6px;
    background: var(--card);
  }
  .card--front .wordmark__square { width: 46px; height: 46px; }
  .card--front .wordmark__name { font-size: 33px; letter-spacing: 1px; }

  .card--back .wordmark { left: 40px; top: 38px; }
  .card--back .wordmark__square { width: 44px; height: 44px; }
  .card--back .wordmark__name { font-size: 30px; letter-spacing: 1px; }

  .back-accent {
    position: absolute;
    right: 0;
    bottom: 0;
    width: 290px;
    height: 346px;
    background: linear-gradient(160deg, rgba(27,47,60,0) 0%, var(--card-tint) 45%, #1d3444 100%);
  }

  .contact-block {
    position: absolute;
    left: 40px;
    top: 126px;
    color: var(--ink-soft);
  }
  .person__name {
    color: var(--accent-blue);
    font-size: 20px;
    font-weight: 700;
    line-height: 24px;
  }
  .person__role {
    font-size: 15px;
    line-height: 20px;
    color: var(--ink-light);
  }
  .divider {
    width: 33px;
    height: 2px;
    background: var(--accent-blue);
    margin: 14px 0 17px;
  }
  .contact-list { list-style: none; }
  .contact-list li {
    display: flex;
    align-items: flex-start;
    gap: 6px;
    font-size: 15px;
    line-height: 21px;
  }
  .contact-list li + li { margin-top: 0; }
  .contact-list .contact--address { margin-bottom: 6px; }
  .icon {
    flex: none;
    width: 13px;
    height: 13px;
    margin-top: 4px;
    stroke: var(--accent-blue);
    fill: none;
    stroke-width: 1.6;
    stroke-linecap: round;
    stroke-linejoin: round;
  }
</style>
</head>
<body>

<section class="card card--front" aria-label="Business card front">
  <div class="front-texture" role="img" aria-label="Tone-on-tone pattern of the company mark fading from silver to dark"></div>
  <div class="wordmark">
    <span class="wordmark__square"></span>
    <span class="wordmark__name">Kelmora Consulting</span>
  </div>
</section>

<section class="card card--back" aria-label="Business card back">
  <div class="back-accent" role="img" aria-label="Large faint company mark decoration"></div>

  <div class="wordmark">
    <span class="wordmark__square"></span>
    <span class="wordmark__name">Kelmora Consulting</span>
  </div>

  <div class="contact-block">
    <p class="person__name">Daniel Carver</p>
    <p class="person__role">President</p>
    <div class="divider"></div>
    <ul class="contact-list">
      <li class="contact--address">
        <svg class="icon" viewBox="0 0 14 14"><path d="M7 13s4.5-4.6 4.5-7.6A4.5 4.5 0 0 0 2.5 5.4C2.5 8.4 7 13 7 13z"/><circle cx="7" cy="5.4" r="1.6"/></svg>
        <span>418 Alder Crest Way, Suite 210<br>Fairmont, CA 95012</span>
      </li>
      <li>
        <svg class="icon" viewBox="0 0 14 14"><path d="M3 1.5l2.2 2.6-1.3 1.6a8 8 0 0 0 4.4 4.4l1.6-1.3 2.6 2.2-1.4 1.5C6 12.2 1.8 8 1.5 2.9z"/></svg>
        <span>555-204-7816</span>
      </li>
      <li>
        <svg class="icon" viewBox="0 0 14 14"><rect x="1.2" y="2.8" width="11.6" height="8.4" rx="0.8"/><path d="M1.5 3.3L7 7.6l5.5-4.3"/></svg>
        <span>daniel@kelmora.com</span>
      </li>
      <li>
        <svg class="icon" viewBox="0 0 14 14"><circle cx="7" cy="7" r="5.7"/><path d="M1.3 7h11.4M7 1.3c-2.6 3-2.6 8.4 0 11.4M7 1.3c2.6 3 2.6 8.4 0 11.4"/></svg>
        <span>www.kelmora.com</span>
      </li>
    </ul>
  </div>
</section>

</body>
</html>
```